KRT Design Business Card

I need to develop a business card for my real estate design and investment company. Something clean, classic and professional with a modern vibe.

Industry/Entity Type

Real Estate

Font styles to use
Serif
Sans Serif

```html
<!DOCTYPE html>
<html lang="en">
<head>
<meta charset="utf-8">
<title>KRT Design Business Card</title>
<link rel="stylesheet" href="https://fonts.googleapis.com/css2?family=Lato:wght@400;700;900&display=swap">
<style>
  :root {
    --canvas: #2b2b2b;
    --card-dark: #3d3d3d;
    --card-light: #f6f6f6;
    --ink-dark: #1f1f1f;
    --ink-mid: #555555;
    --ink-light: #e9e9e9;
    --ink-soft: #bdbdbd;
    --skyline-light: #ececec;
    --skyline-dark: #3a3a3a;
  }
  * { box-sizing: border-box; margin: 0; padding: 0; }
  html, body {
    width: 1200px; height: 997px; overflow: hidden;
    background: var(--canvas);
    font-family: "Lato", Arial, sans-serif;
  }
  .stage {
    width: 1200px; height: 997px;
    display: flex; flex-direction: column;
    align-items: center; justify-content: center; gap: 60px;
  }
  .card {
    position: relative;
    width: 640px; height: 366px;
    overflow: hidden;
    box-shadow: 0 10px 28px rgba(0,0,0,0.45);
  }
  .card--back { background: var(--card-dark); color: var(--ink-light); }
  .card--front { background: var(--card-light); color: var(--ink-dark); }

  .brand {
    position: absolute;
    display: flex; align-items: center; gap: 14px;
    font-weight: 400; letter-spacing: 2px; white-space: nowrap;
  }
  .brand__square { width: 22px; height: 22px; border: 2px solid currentColor; }
  .card--back .brand { left: 130px; top: 88px; font-size: 44px; }
  .card--front .brand { left: 50%; transform: translateX(-50%); top: 58px; font-size: 42px; }

  .tagline {
    position: absolute; right: 60px; top: 206px;
    font-size: 13px; letter-spacing: 4px; color: var(--ink-soft);
    white-space: nowrap;
  }

  .skyline { position: absolute; left: 0; bottom: 0; width: 100%; }
  .skyline--light { height: 120px; background: linear-gradient(to top, var(--skyline-light) 70%, #cfcfcf); }
  .skyline--dark { height: 62px; background: linear-gradient(to top, var(--skyline-dark) 70%, #5a5a5a); }

  .holder { position: absolute; right: 60px; top: 168px; text-align: right; }
  .holder__name { font-size: 22px; font-weight: 900; color: #333; }
  .holder__role { font-size: 12px; font-weight: 700; letter-spacing: 1px; color: var(--ink-mid); margin-top: 2px; }

  .contacts { position: absolute; left: 52px; top: 212px; list-style: none; }
  .contacts li {
    display: flex; align-items: center; gap: 14px;
    font-size: 15px; font-weight: 700; color: #333;
    height: 27px;
  }
  .contacts svg { width: 18px; height: 18px; flex: none; }
</style>
</head>
<body>
<main class="stage">

  <section class="card card--back" aria-label="Business card back">
    <div class="brand"><span class="brand__square"></span>KRT Design</div>
    <p class="tagline">WE BUILD VALUE THAT LASTS</p>
    <div class="skyline skyline--light" role="img" aria-label="City skyline silhouette"></div>
  </section>

  <section class="card card--front" aria-label="Business card front">
    <div class="brand"><span class="brand__square"></span>KRT Design</div>
    <div class="holder">
      <p class="holder__name">Dana Whitfield</p>
      <p class="holder__role">DIRECTOR</p>
    </div>
    <ul class="contacts">
      <li>
        <svg viewBox="0 0 18 18" aria-hidden="true"><rect x="4" y="1.5" width="10" height="15" rx="2" fill="none" stroke="#333" stroke-width="1.8"/></svg>
        0412555208
      </li>
      <li>
        <svg viewBox="0 0 18 18" aria-hidden="true"><rect x="1.5" y="4" width="15" height="10" fill="#333"/><path d="M1.5 4 L9 10 L16.5 4" fill="none" stroke="#f6f6f6" stroke-width="1.4"/></svg>
        dana@krtdesign.com
      </li>
      <li>
        <svg viewBox="0 0 18 18" aria-hidden="true"><g fill="none" stroke="#333" stroke-width="2" stroke-linecap="round"><path d="M7.5 10.5 L10.5 7.5"/><path d="M8 5 L10 3 A3 3 0 0 1 15 8 L13 10"/><path d="M10 13 L8 15 A3 3 0 0 1 3 10 L5 8"/></g></svg>
        www.krtdesign.com
      </li>
    </ul>
    <div class="skyline skyline--dark" role="img" aria-label="City skyline silhouette"></div>
  </section>

</main>
</body>
</html>
```